Personal training poster - 1200X900mm

Poster to promote my new personal training service at my gym. The poster will be printed and put into an aframe to be seen by people walking past my gym. It needs to be simple and eye catching with the text i have put in the must haves. The text and image should be the prominent parts of the design.

Target Market(s)

30-50 year old females

Industry/Entity Type

Fitness

Font styles to use
Sans Serif

Requirements
Must have
• my logo
• exercise graphic
• Must include the following text:
• Are you looking for a personal trainer? Our expert trainers can help you achieve you take your health and fitness back!
• Contact details:
• 1300452968
• info@brightmovegym.com.au
• Located under the Harbourview Club

```html
<!DOCTYPE html>
<html lang="en">
<head>
<meta charset="utf-8">
<title>Personal Training Poster</title>
<link rel="stylesheet" href="https://fonts.googleapis.com/css2?family=Exo+2:wght@300;400;700;800&display=swap">
<style>
  :root {
    --paper: #fde88f;
    --glow: #fff6c8;
    --brand-blue: #1f5aaf;
    --accent-red: #e4584a;
    --ink: #1b1b1b;
  }
  html, body {
    margin: 0;
    padding: 0;
    overflow: hidden;
    background: #ffffff;
  }
  .poster {
    position: relative;
    width: 913px;
    height: 1200px;
    background: var(--paper);
    font-family: "Exo 2", sans-serif;
    color: var(--ink);
    overflow: hidden;
  }
  .exercise-graphic {
    position: absolute;
    left: 71px;
    top: 26px;
    width: 779px;
    height: 146px;
    border-radius: 14px;
    background: linear-gradient(90deg, #e4584a 0%, #2a62b4 30%, #e4584a 55%, #2a62b4 78%, #e4584a 100%);
    opacity: 0.85;
  }
  .headline {
    position: absolute;
    left: 0;
    right: 0;
    top: 188px;
    margin: 0;
    text-align: center;
    font-weight: 800;
    font-size: 106px;
    line-height: 93px;
    letter-spacing: -3px;
    color: var(--brand-blue);
    text-transform: uppercase;
  }
  .tagline {
    position: absolute;
    left: 0;
    right: 0;
    top: 592px;
    margin: 0;
    text-align: center;
    font-weight: 300;
    font-size: 36px;
    line-height: 46px;
  }
  .logo-glow {
    position: absolute;
    left: 256px;
    top: 690px;
    width: 400px;
    height: 280px;
    background: radial-gradient(ellipse at center, var(--glow) 0%, rgba(255,246,200,0) 70%);
  }
  .brand {
    position: absolute;
    left: 0;
    right: 0;
    top: 800px;
    display: flex;
    justify-content: center;
    align-items: center;
    gap: 14px;
  }
  .brand-dot {
    width: 38px;
    height: 38px;
    border-radius: 50%;
    background: var(--brand-blue);
  }
  .brand-name {
    font-weight: 800;
    font-size: 42px;
    color: var(--brand-blue);
    text-transform: uppercase;
    letter-spacing: -1px;
  }
  .contact {
    position: absolute;
    left: 0;
    right: 0;
    top: 934px;
    text-align: center;
  }
  .contact-label {
    margin: 0;
    font-weight: 400;
    font-size: 38px;
    line-height: 52px;
  }
  .contact-phone {
    margin: 6px 0 0;
    font-weight: 700;
    font-size: 58px;
    line-height: 66px;
    color: var(--accent-red);
  }
  .contact-line {
    margin: 0;
    font-weight: 300;
    font-size: 38px;
    line-height: 50px;
  }
</style>
</head>
<body>
  <main class="poster">
    <div class="exercise-graphic" role="img" aria-label="Row of exercise icons: dumbbells, water bottle, running shoe and barbell"></div>

    <h1 class="headline">Are you<br>looking for a<br>personal<br>trainer?</h1>

    <p class="tagline">Our expert trainers can help you get<br>your health and fitness back!</p>

    <div class="logo-glow"></div>
    <div class="brand">
      <span class="brand-dot"></span>
      <span class="brand-name">Brightmove Gym</span>
    </div>

    <section class="contact">
      <p class="contact-label">Contact details:</p>
      <p class="contact-phone">1300 452 968</p>
      <p class="contact-line">info@brightmovegym.com.au</p>
      <p class="contact-line">Located under the Harbourview Club</p>
    </section>
  </main>
</body>
</html>
```